Business Card Design

Quiet Meadows - edgy, unique, ontrend clothing for girls 0-12.
I would like simple styling with white background and natural beige/brown font, similar to attached font.

Industry/Entity Type

Clothing

Contact Information for Business Card

Hi, I would like a very simple business card, white background with natural, beige, brown font, Quiet Meadows. I design and sell clothes for girls 0-12 with a touch of bohemian styling. I would like "Quiet Meadows" on front and on back -
www.quietmeadows-example.com.au
Delia Hartwell,
0481552937,
deliahartwell@brightnest-mail.com.au

```html
<!DOCTYPE html>
<html lang="en">
<head>
<meta charset="utf-8">
<title>Quiet Meadows – Business Card</title>
<link rel="stylesheet" href="https://fonts.googleapis.com/css2?family=Indie+Flower&family=Quicksand:wght@500&display=swap">
<style>
  :root {
    --backdrop: #ece8e2;
    --card: #ffffff;
    --olive-beige: #b7b088;
    --blossom-pink: #dc8c9c;
    --ink-grey: #8a8580;
    --leaf-soft: #e4e2cf;
    --petal-soft: #f3d3d8;
    --swirl-soft: #e8ddd6;
  }
  * { box-sizing: border-box; margin: 0; padding: 0; }
  html, body { width: 1200px; height: 776px; overflow: hidden; }
  body {
    background: var(--backdrop);
    position: relative;
    font-family: "Quicksand", sans-serif;
  }
  .card {
    position: absolute;
    top: 234px;
    width: 540px;
    height: 308px;
    background: var(--card);
    box-shadow: 0 6px 18px rgba(60, 40, 20, 0.18);
    overflow: hidden;
  }
  .card--front { left: 40px; }
  .card--back { left: 620px; }

  .ornament {
    position: absolute;
    border-radius: 50%;
  }
  .ornament--front-top {
    top: -40px; right: -30px; width: 230px; height: 150px;
    background: radial-gradient(ellipse at 60% 40%, var(--petal-soft) 0%, var(--leaf-soft) 45%, rgba(255,255,255,0) 72%);
  }
  .ornament--front-bottom {
    bottom: -50px; left: -40px; width: 270px; height: 160px;
    background: radial-gradient(ellipse at 45% 55%, var(--petal-soft) 0%, var(--leaf-soft) 45%, rgba(255,255,255,0) 72%);
  }
  .ornament--back-sweep {
    top: -60px; left: -60px; width: 480px; height: 420px;
    background: radial-gradient(ellipse at 30% 45%, var(--petal-soft) 0%, var(--swirl-soft) 35%, var(--leaf-soft) 55%, rgba(255,255,255,0) 72%);
  }

  .brand-name {
    position: absolute;
    top: 118px; left: 0; width: 100%;
    text-align: center;
    font-family: "Indie Flower", cursive;
    font-size: 64px;
    line-height: 1;
    color: var(--olive-beige);
  }

  .contact {
    position: absolute;
    right: 30px; top: 108px;
    text-align: right;
  }
  .contact__name {
    font-family: "Indie Flower", cursive;
    font-size: 48px;
    line-height: 1;
    color: var(--blossom-pink);
  }
  .contact__web {
    font-family: "Indie Flower", cursive;
    font-size: 26px;
    color: var(--blossom-pink);
    margin-top: 2px;
  }
  .contact__line {
    font-size: 13px;
    color: var(--ink-grey);
    margin-top: 8px;
  }
  .contact__label { color: var(--blossom-pink); }
</style>
</head>
<body>
  <section class="card card--front" aria-label="Business card front">
    <div class="ornament ornament--front-top" role="img" aria-label="Floral swirl ornament with pink blossom and sage leaves"></div>
    <div class="ornament ornament--front-bottom" role="img" aria-label="Floral swirl ornament with pink blossom and sage leaves"></div>
    <h1 class="brand-name">Quiet Meadows</h1>
  </section>

  <section class="card card--back" aria-label="Business card back">
    <div class="ornament ornament--back-sweep" role="img" aria-label="Sweeping floral swirls with pink blossom and sage leaves"></div>
    <div class="contact">
      <p class="contact__name">Delia Hartwell</p>
      <p class="contact__web">www.quietmeadows-example.com.au</p>
      <p class="contact__line"><span class="contact__label">Phone:</span> 0481552937</p>
      <p class="contact__line"><span class="contact__label">E-mail:</span> deliahartwell@brightnest-mail.com.au</p>
    </div>
  </section>
</body>
</html>
```